Quimby's Yard & Garden Center Business Card Update

I need an updated Business card design for my Lawn and Garden Center. We do Landscaping installs, Lawn Mowing, Snow Removal and also have a Garden Center Retail Division. I uploaded a few of our previous business cards to give an idea of what we are starting with. The main goal of this update is to simplify and modernize the business card, not all of the services that are on the previous cards has to be on the new one but I would still like to highlight our main services. There is also a sample of our logo that Can be used in the design.

Industry/Entity Type

Landscaping

Contact Information for Business Card

Morris Quimby
Morris@Quimbysyardandgarden.example
Business (555) 201-7784
Cell (555) 318-6092

Colors

Designer to choose colors to be used in the design.

Requirements
Must have
• Services Provided :
• Landscaping
• Lawn Maintenance
• Snow Removal
• Garden Center

```html
<!DOCTYPE html>
<html lang="en">
<head>
<meta charset="utf-8">
<title>Quimby's Yard &amp; Garden Center – Business Card</title>
<link rel="stylesheet" href="https://fonts.googleapis.com/css2?family=Nunito+Sans:wght@300;400;600&display=swap">
<style>
  :root {
    --backdrop: #8f8f8f;
    --forest: #2f5128;
    --paper: #ffffff;
    --ink-black: #000000;
    --card-w: 710px;
    --card-h: 405px;
  }
  * { box-sizing: border-box; margin: 0; padding: 0; }
  html, body {
    width: 1200px; height: 960px; overflow: hidden;
    background: var(--backdrop);
    font-family: "Nunito Sans", "Avenir Next", sans-serif;
  }
  .card {
    position: absolute;
    left: 245px;
    width: var(--card-w); height: var(--card-h);
    border-radius: 24px;
    overflow: hidden;
  }
  .card--front { top: 60px; background: var(--paper); }
  .card--back { top: 515px; background: var(--ink-black); color: var(--paper); }

  .front-wave { position: absolute; inset: 0; }

  .contact-block {
    position: absolute; left: 68px; top: 168px;
    color: var(--paper);
  }
  .contact-name { font-size: 27px; font-weight: 600; line-height: 1.2; }
  .contact-role { font-size: 19px; font-weight: 300; margin-top: 2px; }
  .contact-list { list-style: none; margin-top: 22px; }
  .contact-list li {
    display: flex; align-items: center; gap: 7px;
    font-size: 17px; font-weight: 300; height: 25.5px;
  }
  .contact-list svg { width: 14px; height: 14px; fill: var(--paper); flex: none; }

  .brand {
    position: absolute;
    display: flex; align-items: center;
    font-weight: 600;
  }
  .brand-dot { border-radius: 50%; flex: none; }
  .brand--front {
    right: 50px; top: 88px;
    color: var(--forest); font-size: 44px; gap: 12px;
  }
  .brand--front .brand-dot { width: 18px; height: 18px; background: var(--forest); }
  .brand--back {
    left: 0; right: 0; top: 150px; justify-content: center;
    color: var(--paper); font-size: 68px; gap: 18px;
  }
  .brand--back .brand-dot { width: 28px; height: 28px; background: var(--forest); }

  .services {
    position: absolute; left: 0; right: 0; top: 298px;
    text-align: center; font-size: 18px; font-weight: 400; line-height: 25px;
  }
</style>
</head>
<body>

<section class="card card--front" aria-label="Business card front">
  <svg class="front-wave" viewBox="0 0 710 405" preserveAspectRatio="none" aria-hidden="true">
    <path fill="var(--forest)" d="M0 0 H215 C205 30 225 55 275 75 C345 100 380 135 345 160 C300 190 300 215 340 235 C400 260 505 250 492 290 C485 310 415 315 432 338 C450 360 555 350 565 405 H0 Z"/>
  </svg>

  <div class="contact-block">
    <h1 class="contact-name">Morris Quimby</h1>
    <p class="contact-role">President</p>
    <ul class="contact-list">
      <li><svg viewBox="0 0 16 16"><path d="M3 2l3 0 1 4-2 1c1 2 2 3 4 4l1-2 4 1 0 3c-6 1-12-5-11-11z"/></svg>(555) 201-7784 (Office)</li>
      <li><svg viewBox="0 0 16 16"><path d="M3 2l3 0 1 4-2 1c1 2 2 3 4 4l1-2 4 1 0 3c-6 1-12-5-11-11z"/></svg>(555) 318-6092 (Cell)</li>
      <li><svg viewBox="0 0 16 16"><path d="M1 4h14v9H1z M2 5l6 4 6-4" stroke="var(--forest)" stroke-width="1"/></svg>Morris@Quimbysyardandgarden.example</li>
      <li><svg viewBox="0 0 16 16"><path fill="none" stroke="var(--paper)" stroke-width="1.3" d="M8 1.5a6.5 6.5 0 1 0 0.01 0z M1.5 8h13 M8 1.5c-3 3-3 10 0 13 M8 1.5c3 3 3 10 0 13 M2.5 4.8h11 M2.5 11.2h11"/></svg>www.Quimbysyardandgarden.example</li>
    </ul>
  </div>

  <div class="brand brand--front"><span class="brand-dot"></span>Quimby's</div>
</section>

<section class="card card--back" aria-label="Business card back">
  <div class="brand brand--back"><span class="brand-dot"></span>Quimby's</div>
  <p class="services">Landscaping&nbsp; - &nbsp;Lawn Maintenance<br>Snow Removal&nbsp; - &nbsp;Garden Center</p>
</section>

</body>
</html>
```